Letterhead design for Sleep Consulting Business

I'm looking for a new letterhead (heading/footer) design for my Sleep Consulting Business, I work with families to help their children improve their sleep.

The heading/footer will used in Microsoft Word Only-to be used for all of my documents such as writing Sleep Plans. I need to utilize as much working space in the document as possible. This will NOT be printed out on paper- it will only be used for heading/footer on microsoft word, then emailed to clients, who may print it at home.

My brand colors:
Dark Blue Hex: 1F2A42
Lighter Blueish Hex: 90BEC9
You're welcome to check out my website for inspiration- it is freshly created with other colors as well, and I love the outcome. www.hollowpinerest.com

Target Market(s)

Tired parents

Font styles to use
Script
Other font styles liked:
• Great Vibe, Lato or Just Another Hand are all used currently for my brand. Open to other options.

Requirements
Must have
• The letterhead (heading/footer) MUST be kept narrow (height-wise), so I have plenty of space on my document, while including important information.

It should look professional on screen, and when printed.

Must include my business name OR logo (Hollow Pine Sleep Consulting), and my email address. Mara@hollowpinerest.com

Website is optional, not required, just if you need to fill in a spot: www.hollowpinerest.com

```html
<!DOCTYPE html>
<html lang="en">
<head>
<meta charset="utf-8">
<title>Hollow Pine Sleep Consulting – Letterhead</title>
<link rel="stylesheet" href="https://fonts.googleapis.com/css2?family=Poppins:wght@400;500&display=swap">
<style>
  :root {
    --navy: #1b2540;
    --mist: #8cb7c3;
    --paper: #f2f2f2;
    --backdrop: #d6dcdd;
    --white: #ffffff;
  }
  * { margin: 0; padding: 0; box-sizing: border-box; }
  html, body { width: 1200px; height: 1200px; overflow: hidden; }
  body {
    background: var(--backdrop);
    font-family: "Poppins", sans-serif;
    position: relative;
  }
  .letterhead {
    position: absolute;
    left: 203px;
    top: 40px;
    width: 793px;
    height: 1120px;
    background: var(--paper);
    overflow: hidden;
  }
  .letterhead-waves {
    position: absolute;
    inset: 0;
    width: 100%;
    height: 100%;
  }
  .brand {
    position: absolute;
    left: 42px;
    top: 76px;
    display: flex;
    align-items: center;
    gap: 14px;
  }
  .brand-dot {
    width: 70px;
    height: 70px;
    border-radius: 50%;
    background: var(--mist);
  }
  .brand-name {
    font-family: "Poppins", sans-serif;
    font-weight: 500;
    font-size: 21px;
    line-height: 1.25;
    color: var(--navy);
  }
  .contact {
    position: absolute;
    left: 32px;
    top: 1064px;
    list-style: none;
    color: var(--white);
    font-size: 13px;
    line-height: 19px;
  }
  .contact li { display: flex; align-items: center; gap: 10px; }
  .contact svg { width: 12px; height: 12px; flex: none; }
</style>
</head>
<body>
  <main class="letterhead">
    <svg class="letterhead-waves" viewBox="0 0 956 1350" preserveAspectRatio="none" aria-hidden="true">
      <!-- header -->
      <path fill="var(--navy)" d="M0,0 H956 V100 C800,105 700,90 560,60 C420,30 300,20 180,40 C100,52 40,65 0,75 Z"/>
      <path fill="var(--mist)" d="M0,82 C60,64 200,36 360,38 C220,40 90,72 0,110 Z"/>
      <path fill="var(--mist)" d="M590,80 C700,104 820,112 956,106 V136 C820,132 700,112 590,80 Z"/>
      <!-- footer -->
      <path fill="var(--mist)" d="M0,1213 C150,1212 260,1240 365,1270 C250,1246 120,1238 0,1243 Z"/>
      <path fill="var(--navy)" d="M0,1252 C200,1247 380,1277 560,1307 C700,1327 850,1322 956,1294 V1350 H0 Z"/>
      <path fill="var(--mist)" d="M600,1310 C760,1314 880,1290 956,1240 V1262 C880,1302 760,1318 600,1310 Z"/>
    </svg>

    <header class="brand">
      <span class="brand-dot"></span>
      <p class="brand-name">Hollow Pine<br>Sleep Consulting</p>
    </header>

    <footer>
      <ul class="contact">
        <li>
          <svg viewBox="0 0 12 12"><rect x="0.5" y="2" width="11" height="8" rx="1" fill="var(--mist)"/><path d="M1 3 L6 7 L11 3" stroke="var(--navy)" stroke-width="1" fill="none"/></svg>
          mara@hollowpinerest.com
        </li>
        <li>
          <svg viewBox="0 0 12 12"><circle cx="6" cy="6" r="5.5" fill="var(--mist)"/><path d="M0.5 6 H11.5 M6 0.5 C3 3 3 9 6 11.5 M6 0.5 C9 3 9 9 6 11.5" stroke="var(--navy)" stroke-width="0.8" fill="none"/></svg>
          www.hollowpinerest.com
        </li>
      </ul>
    </footer>
  </main>
</body>
</html>
```